Construction Business Card Design

We need a business card design for a new company based in Dallas/Ft Worth, Texas called Calloway Brinn Construction. We are a commercial construction design/build general contractor. We construct warehouse, office, manufacturing, tenant improvements, tenant finish-out, remodeling.

Reason: Additional designs, would like to see one incorporating CB as logo but keep actual company name on card as well thanks

Target Market(s)

Developers/Business Owners

Industry/Entity Type

Construction

Contact Information for Business Card

CALLOWAY BRINN CONSTRUCTION, Neil Marsten, 4817 FM 622, Ste 318, Bartonville, TX 76226 Mailing: 7342 Cedar Gulch Road, Briar Hollow, 75412,Office-940-362-8146, M-214-693-2581, F-817-524-1039, neil@callowaybrinn.example, www.callowaybrinn.example

Requirements
Must have
• Color/Stand out/Unique
Nice to have
• Logo uploaded is a first shot at design but the mountain is not a requirement

```html
<!DOCTYPE html>
<html lang="en">
<head>
<meta charset="utf-8">
<title>Calloway Brinn Construction — Business Card</title>
<link rel="stylesheet" href="https://fonts.googleapis.com/css2?family=Libre+Baskerville:wght@400;700&family=Open+Sans:wght@400;600&display=swap">
<style>
  :root {
    --stage: #161616;
    --card-black: #0d0d0d;
    --card-white: #ffffff;
    --brand-green: #0d4a2e;
    --ink: #1c1c1c;
    --white: #ffffff;
    --rule: #b9c7bf;
  }
  * { box-sizing: border-box; margin: 0; padding: 0; }
  html, body { width: 1200px; height: 900px; overflow: hidden; }
  body {
    background: var(--stage);
    display: flex;
    flex-direction: column;
    align-items: center;
    justify-content: center;
    gap: 60px;
  }
  .card {
    position: relative;
    width: 560px;
    height: 320px;
    border-radius: 18px;
    overflow: hidden;
    box-shadow: 0 14px 30px rgba(0,0,0,.55);
  }

  /* Back */
  .card--back { background: var(--card-black); }
  .card--back .brand {
    position: absolute;
    left: 120px;
    top: 118px;
  }

  /* Brand lockup */
  .brand { display: flex; align-items: center; gap: 14px; }
  .brand__dot {
    width: 62px; height: 62px; border-radius: 50%;
    background: var(--brand-green);
    flex: none;
  }
  .brand__name {
    font-family: "Libre Baskerville", serif;
    font-weight: 700;
    line-height: 1.05;
    letter-spacing: .02em;
  }
  .brand__name span { display: block; }
  .brand__name .brand__sub { font-size: .68em; letter-spacing: .22em; }
  .card--back .brand__name { color: var(--white); font-size: 22px; }

  /* Front */
  .card--front { background: var(--card-white); }
  .front__band {
    position: absolute;
    left: 44px; top: 0;
    width: 96px; height: 100%;
    background: var(--brand-green);
  }
  .front__band-cap {
    position: absolute;
    left: 44px; top: 0;
    width: 96px; height: 56px;
    background: var(--card-black);
  }
  .card--front .brand {
    position: absolute;
    left: 112px;
    top: 22px;
  }
  .card--front .brand__dot { width: 56px; height: 56px; border: 4px solid var(--white); }
  .card--front .brand__name { color: var(--brand-green); font-size: 20px; }

  .front__person {
    position: absolute;
    left: 170px;
    top: 148px;
    font-family: "Libre Baskerville", serif;
    font-weight: 700;
    font-size: 19px;
    color: var(--brand-green);
  }
  .front__divider {
    position: absolute;
    left: 330px;
    top: 196px;
    width: 1px;
    height: 72px;
    background: var(--rule);
  }
  .front__contact {
    position: absolute;
    left: 350px;
    top: 200px;
    font-family: "Open Sans", sans-serif;
    font-size: 13px;
    line-height: 1.45;
    color: var(--ink);
    list-style: none;
  }
  .front__contact .gap { margin-top: 6px; }
  .front__contact li { display: flex; align-items: center; gap: 7px; }
  .tag {
    width: 15px; height: 15px; border-radius: 50%;
    background: var(--brand-green);
    color: var(--white);
    font-size: 9px; font-weight: 600;
    display: inline-flex; align-items: center; justify-content: center;
  }
</style>
</head>
<body>

  <section class="card card--back" aria-label="Business card back">
    <div class="brand">
      <div class="brand__dot" aria-hidden="true"></div>
      <div class="brand__name">
        <span>CALLOWAY BRINN</span>
        <span class="brand__sub">CONSTRUCTION</span>
      </div>
    </div>
  </section>

  <section class="card card--front" aria-label="Business card front">
    <div class="front__band"></div>
    <div class="front__band-cap"></div>

    <div class="brand">
      <div class="brand__dot" aria-hidden="true"></div>
      <div class="brand__name">
        <span>CALLOWAY BRINN</span>
        <span class="brand__sub">CONSTRUCTION</span>
      </div>
    </div>

    <p class="front__person">Neil Marsten</p>

    <div class="front__divider"></div>

    <ul class="front__contact">
      <li>7342 Cedar Gulch Road</li>
      <li>Briar Hollow, 75412</li>
      <li class="gap"><span class="tag">M</span>214-693-2581</li>
      <li><span class="tag">F</span>817-524-1039</li>
    </ul>
  </section>

</body>
</html>
```